business card

Business card for new business.
Red and black corporate colors.
Card can have an Indsutrial feel to it. Feel free to add Rust, Bolted steel, or graphics as you see fit. We provide highly specialized services to the below mentioned industries.
Keep information out of corners so that if I want I can choose rounded corners.
Information
- front. name - title - phone - email
- Rear
Refining - Rail - Infrastructure - Mining - Energy
Calgary - Edmonton - Fort McMurray - Revelstoke - Vancouver

```html
<!DOCTYPE html>
<html lang="en">
<head>
<meta charset="utf-8">
<title>Ironspan Business Card</title>
<link rel="stylesheet" href="https://fonts.googleapis.com/css2?family=Roboto+Condensed:wght@700&family=Roboto:wght@400;700&display=swap">
<style>
  :root {
    --page-bg: #d9d6d2;
    --card-black: #141516;
    --card-charcoal: #2a2c2f;
    --accent-red: #e0141e;
    --rust-red: #8e0c12;
    --muted-grey: #8a8a8a;
    --logo-grey: #8c8c8c;
    --text-white: #f2f2f2;
    --rule: #4a4c50;
  }
  * { margin: 0; padding: 0; box-sizing: border-box; }
  html, body { width: 1200px; height: 960px; overflow: hidden; }
  body { background: var(--page-bg); position: relative; font-family: "Roboto", Arial, sans-serif; }

  .card {
    position: absolute;
    width: 600px;
    height: 342px;
    background: var(--card-black);
    overflow: hidden;
  }
  .card--front { left: 303px; top: 129px; }
  .card--back { left: 299px; top: 489px; }

  .card__texture {
    position: absolute; inset: 0;
    background:
      radial-gradient(ellipse 55% 50% at 50% 52%, var(--card-charcoal) 0%, rgba(20,21,22,0) 100%),
      linear-gradient(180deg, rgba(142,12,18,0.75) 0%, rgba(142,12,18,0.15) 22%, rgba(20,21,22,0) 45%, rgba(20,21,22,0) 70%, rgba(142,12,18,0.35) 100%),
      radial-gradient(ellipse 18% 25% at 0% 65%, rgba(142,12,18,0.55), rgba(0,0,0,0)),
      radial-gradient(ellipse 18% 25% at 100% 35%, rgba(142,12,18,0.5), rgba(0,0,0,0)),
      var(--card-black);
  }

  .identity {
    position: absolute; left: 10px; top: 128px; width: 260px;
    text-align: right; white-space: nowrap;
  }
  .identity__name {
    font-family: "Roboto Condensed", "Arial Narrow", sans-serif;
    font-weight: 700; font-size: 30px; line-height: 34px;
    color: var(--accent-red); letter-spacing: 0.2px;
  }
  .identity__title {
    font-family: "Roboto Condensed", "Arial Narrow", sans-serif;
    font-weight: 700; font-size: 17px; line-height: 20px;
    color: var(--muted-grey); margin-top: 2px;
  }

  .contact { position: absolute; left: 292px; top: 127px; list-style: none; }
  .contact__item {
    display: flex; align-items: center; gap: 9px;
    font-size: 14.5px; line-height: 19px; color: var(--text-white);
    white-space: nowrap;
  }
  .contact__icon { width: 12px; height: 12px; fill: var(--accent-red); flex: none; }

  .divider {
    position: absolute; left: 70px; top: 232px; width: 458px; height: 1px;
    background: var(--rule);
  }

  .services {
    position: absolute; left: 0; top: 254px; width: 100%;
    text-align: center;
    font-family: "Roboto", Arial, sans-serif; font-weight: 700;
    font-size: 13.5px; line-height: 18px; color: var(--accent-red);
    text-transform: uppercase; white-space: nowrap;
  }

  .brand {
    position: absolute; left: 0; top: 0; width: 100%; height: 100%;
    display: flex; align-items: center; justify-content: center;
    padding-top: 4px;
  }
  .brand__name {
    font-family: "Roboto Condensed", "Arial Narrow", sans-serif;
    font-weight: 700; font-size: 60px; letter-spacing: 1px;
    color: var(--logo-grey); text-transform: uppercase;
  }
</style>
</head>
<body>
  <section class="card card--front">
    <div class="card__texture" role="img" aria-label="Dark carbon steel texture with red rust splatter along the edges"></div>

    <div class="identity">
      <div class="identity__name">DALE HARKER</div>
      <div class="identity__title">CEO/FOUNDER</div>
    </div>

    <ul class="contact">
      <li class="contact__item">
        <svg class="contact__icon" viewBox="0 0 12 12" aria-hidden="true"><path d="M2.4 0.6l2 2.2-1.1 1.4c0.8 1.7 2 2.9 3.6 3.7l1.4-1.1 2.2 2-1.3 2.4C5 10.7 1.3 7 0.1 1.9z"/></svg>
        <span>587 210 4419</span>
      </li>
      <li class="contact__item">
        <svg class="contact__icon" viewBox="0 0 12 12" aria-hidden="true"><path d="M0 2.5h12v7H0z M0.6 2.8L6 6.8l5.4-4" fill="var(--accent-red)" stroke="var(--card-black)" stroke-width="1"/></svg>
        <span>info@ironspan.com</span>
      </li>
      <li class="contact__item">
        <svg class="contact__icon" viewBox="0 0 12 12" aria-hidden="true"><circle cx="6" cy="6" r="6"/><path d="M6 0.5v11M0.5 6h11M6 0.5c-3 3-3 8 0 11M6 0.5c3 3 3 8 0 11" fill="none" stroke="var(--card-black)" stroke-width="0.9"/></svg>
        <span>www.ironspan.com</span>
      </li>
    </ul>

    <div class="divider"></div>

    <p class="services">
      Forging | Marine | Pipelines | Quarrying<br>
      Power | Brookfield | Lakemont | Port Halden<br>
      Ridgeway | Westmere
    </p>
  </section>

  <section class="card card--back">
    <div class="card__texture" role="img" aria-label="Dark carbon steel texture with red rust splatter along the edges"></div>
    <div class="brand">
      <span class="brand__name">Ironspan</span>
    </div>
  </section>
</body>
</html>
```